Property Management Company Business Cards

Need business cards for a property management company located in Michigan. We manage houses for clients all over the world. Young and modern company, looking for eye catching design. Please work with the attached logo.

Industry/Entity Type

Property Management

Requirements
Must have
• Need lines for address, telephone number, fax number, web site.

Also lines for name, and job title

```html
<!DOCTYPE html>
<html lang="en">
<head>
<meta charset="utf-8">
<title>Lakeshore Harbor Management – Business Cards</title>
<link rel="stylesheet" href="https://fonts.googleapis.com/css2?family=Open+Sans:wght@400;600;700&display=swap">
<style>
  :root {
    --backdrop: #c6d1d9;
    --card-dark: #38393d;
    --card-light: #ffffff;
    --accent-blue: #1aa6e4;
    --accent-green: #8cc63f;
    --text-light: #ffffff;
  }
  * { margin: 0; padding: 0; box-sizing: border-box; }
  html, body {
    width: 1200px; height: 965px; overflow: hidden;
    background: var(--backdrop);
    font-family: "Open Sans", Arial, sans-serif;
  }
  .stage { position: relative; width: 1200px; height: 965px; }
  .card { position: absolute; left: 295px; width: 616px; height: 352px; overflow: hidden; }

  /* Front */
  .card-front { top: 98px; background: var(--card-dark); color: var(--text-light); }
  .brand { position: absolute; left: 240px; top: 42px; display: flex; align-items: center; gap: 10px; }
  .brand-mark { width: 54px; height: 54px; border-radius: 50%; border: 7px solid var(--text-light); }
  .brand-name { color: var(--text-light); font-weight: 700; line-height: 1.05; }
  .brand-name .line-1 { display: block; font-size: 27px; }
  .brand-name .line-2 { display: block; font-size: 12px; letter-spacing: 12.6px; }
  .name-tab { position: absolute; left: 0; top: 173px; width: 14px; height: 58px; background: var(--accent-green); border-radius: 0 6px 6px 0; }
  .person { position: absolute; left: 39px; top: 177px; }
  .person-name { font-size: 19px; color: var(--accent-green); font-weight: 400; line-height: 1.2; }
  .person-title { font-size: 10px; font-weight: 700; margin-left: 4px; }
  .address { position: absolute; left: 39px; top: 275px; font-size: 14px; }
  .address .fill-line { display: inline-block; width: 142px; border-bottom: 1px solid var(--text-light); margin-left: 4px; }
  .website { position: absolute; left: 39px; top: 301px; font-size: 14px; color: var(--accent-blue); }
  .contacts { position: absolute; left: 393px; list-style: none; font-size: 14px; }
  .contacts li { position: absolute; display: flex; align-items: center; gap: 8px; white-space: nowrap; }
  .contacts svg { width: 18px; height: 18px; fill: var(--accent-blue); }

  /* Back */
  .card-back { top: 516px; background: var(--card-light); }
  .back-mark { position: absolute; left: -150px; top: -118px; width: 300px; height: 300px; border-radius: 50%; border: 34px solid var(--card-dark); }
  .back-brand { position: absolute; right: 6px; top: 158px; color: var(--card-dark); font-weight: 700; line-height: 1.05; text-align: right; }
  .back-brand .line-1 { display: block; font-size: 30px; }
  .back-brand .line-2 { display: block; font-size: 14px; letter-spacing: 17px; }
  .back-band { position: absolute; left: 0; bottom: 0; width: 100%; height: 34px; background: var(--card-dark); display: flex; align-items: center; justify-content: center; }
  .back-band .website { position: static; font-size: 15px; }
</style>
</head>
<body>
<main class="stage">
  <section class="card card-front" aria-label="Business card front">
    <div class="brand">
      <span class="brand-mark" aria-hidden="true"></span>
      <span class="brand-name"><span class="line-1">LAKESHORE HARBOR</span><span class="line-2">MANAGEMENT</span></span>
    </div>
    <span class="name-tab" aria-hidden="true"></span>
    <div class="person">
      <p class="person-name">Daniel Reeve</p>
      <p class="person-title">Manager/Director</p>
    </div>
    <p class="address">Address :<span class="fill-line"></span></p>
    <p class="website">www.yourdomain.com</p>
    <ul class="contacts">
      <li style="top:240px;left:-12px;">
        <svg viewBox="0 0 24 24" aria-hidden="true"><path d="M6.6 10.8c1.4 2.8 3.8 5.1 6.6 6.6l2.2-2.2c.3-.3.7-.4 1-.2 1.1.4 2.3.6 3.6.6.6 0 1 .4 1 1V20c0 .6-.4 1-1 1C10.6 21 3 13.4 3 4c0-.6.4-1 1-1h3.5c.6 0 1 .4 1 1 0 1.3.2 2.5.6 3.6.1.3 0 .7-.2 1z"/></svg>
        <span>444-555-666</span>
      </li>
      <li style="top:281px;left:-12px;">
        <svg viewBox="0 0 24 24" aria-hidden="true"><path d="M6 3h12v5H6zM4 9h16a2 2 0 0 1 2 2v6h-4v4H6v-4H2v-6a2 2 0 0 1 2-2zm4 7v3h8v-3z"/></svg>
        <span>444-555-666</span>
      </li>
      <li style="top:303px;left:-12px;">
        <svg viewBox="0 0 24 24" aria-hidden="true"><path d="M2 5h20v14H2zm2 2v.5l8 5.5 8-5.5V7z"/></svg>
        <span>email@email.com</span>
      </li>
    </ul>
  </section>

  <section class="card card-back" aria-label="Business card back">
    <span class="back-mark" aria-hidden="true"></span>
    <div class="back-brand"><span class="line-1">LAKESHORE HARBOR</span><span class="line-2">MANAGEMENT</span></div>
    <div class="back-band"><p class="website">www.yourdomain.com</p></div>
  </section>
</main>
</body>
</html>
```